label design for oral care product

Kindly invite you to design bottle label (114 mm*40 mm) for our product, a kind of oral care product. The GEL is different from our previous cleanser product, as the pic we uploaded for demonstration. The color of frosted glass bottle is dark green, but the cap is white. You could download the pic of bottle among the uploaded files. The logo file and label content description are attached too. Please check them. Our product is made from many kinds of natural plant extracts, which includes herb and fruit. I wish the label would make our product look high-end and reliable. And it would be better if you could give some advice on paper material and special requirements for printing, related to your design. I value the texture of label too, because I think that stands for the quality of products. No color limitation for the use of our logo.
Target Market(s)
20-40 female, who value oral health.
Colors
Designer to choose colors to be used in the design.
Look and feel
Each slider illustrates characteristics of the customer's brand and the style your logo design should communicate.

```html
<!DOCTYPE html>
<html lang="en">
<head>
<meta charset="utf-8">
<title>Aligner Gel Label</title>
<link href="https://fonts.googleapis.com/css2?family=Roboto:wght@400;500;700&family=Roboto+Condensed:wght@500;700;800;900&display=swap" rel="stylesheet">
<style>
  :root {
    --backdrop: #3a3a3c;
    --paper: #ffffff;
    --charcoal: #3d3d3f;
    --ink: #231f20;
    --text-dark: #2e2e2e;
    --text-light: #ffffff;
    --blue-deep: #0e62b0;
    --blue-mid: #1a8fd6;
    --blue-cyan: #13b4e8;
  }
  * { margin: 0; padding: 0; box-sizing: border-box; }
  html, body {
    width: 1200px; height: 554px; overflow: hidden;
    background: var(--backdrop);
  }
  .label {
    position: absolute; left: 103px; top: 103px;
    width: 994px; height: 348px;
    border-radius: 46px; overflow: hidden;
    background: var(--paper);
    box-shadow: 0 14px 24px rgba(0,0,0,0.55);
  }
  .label-art { position: absolute; inset: 0; }
  .text-block {
    position: absolute; text-align: center;
    font-family: 'Roboto', sans-serif; font-size: 17.5px; line-height: 22px;
  }
  .text-block h2 { font-size: 18px; font-weight: 700; line-height: 22px; }
  .contains { left: 25px; top: 30px; width: 270px; color: var(--text-dark); }
  .directions { left: 707px; top: 122px; width: 270px; color: var(--text-light); }
  .directions h2 { margin-bottom: 10px; }
  .brand {
    position: absolute; left: 398px; top: 0; width: 198px; height: 112px;
    display: flex; align-items: center; justify-content: center; gap: 8px;
    font-family: 'Roboto', sans-serif; font-weight: 700; font-size: 28px;
    color: var(--text-light);
  }
  .brand-dot { width: 12px; height: 12px; border-radius: 50%; background: var(--text-light); }
  .claims {
    position: absolute; left: 347px; width: 300px; text-align: center;
    font-family: 'Roboto Condensed', sans-serif; font-weight: 500;
    color: var(--text-light); font-size: 17px; line-height: 20px;
  }
  .claims.tagline { top: 217px; }
  .claims.benefit { top: 250px; }
  .volume {
    position: absolute; left: 397px; top: 314px; width: 200px; text-align: center;
    font-family: 'Roboto Condensed', sans-serif; font-weight: 700; font-size: 16px;
    color: var(--text-dark);
  }
</style>
</head>
<body>
  <div class="label">
    <svg class="label-art" width="994" height="348" viewBox="0 0 994 348">
      <defs>
        <linearGradient id="wedge" x1="0" y1="0" x2="1" y2="0">
          <stop offset="0" stop-color="#c8c8c8"/>
          <stop offset="0.45" stop-color="#4a4a4c"/>
          <stop offset="1" stop-color="#3d3d3f"/>
        </linearGradient>
        <linearGradient id="stripe" x1="0" y1="0" x2="1" y2="0">
          <stop offset="0" stop-color="#13b4e8"/>
          <stop offset="0.5" stop-color="#1a8fd6"/>
          <stop offset="1" stop-color="#0e62b0"/>
        </linearGradient>
      </defs>
      <polygon points="0,278 994,40 994,307 0,307" fill="url(#wedge)"/>
      <polygon points="0,279 994,5 994,40" fill="url(#stripe)"/>
      <polygon points="398,0 596,0 596,104 398,142" fill="var(--ink)"/>
      <rect x="65" y="234" width="189" height="89" fill="#1a8fd6" opacity="0.95"/>
      <text x="497" y="188" text-anchor="middle"
            font-family="'Roboto Condensed', sans-serif" font-weight="900" font-size="60"
            fill="#111" stroke="#1a8fd6" stroke-width="11" stroke-linejoin="round"
            paint-order="stroke">Aligner Gel</text>
    </svg>

    <div class="brand"><span>Froth Leaf</span><span class="brand-dot"></span></div>

    <div class="text-block contains">
      <h2>CONTAINS:</h2>
      <p>a proprietary blend of<br>natural plant extract<br>including Angelica, Radix<br>Rehmanniae, Coptis,<br>Honeysuckle, Echinacea,<br>Sage, Chamomile,<br>Acerola cherry.</p>
    </div>

    <p class="claims tagline">Immune Support for Oral Health</p>
    <p class="claims benefit">Solution to Maintain Dental<br>Hygiene and Strengthen Gums</p>

    <div class="text-block directions">
      <h2>DIRECTIONS:</h2>
      <p>Drop on the teeth<br>directly after brushing.<br>Or, put into clear<br>aligners before wearing<br>again. No need to rinse<br>your mouth with water.</p>
    </div>

    <p class="volume">30 ml / 1 fl oz</p>
  </div>
</body>
</html>
```